pop up booking component and calendar re-design

we have a calander view where a parent cant reserve a day
you can click on please redesign the calander / voucher and pop up.

the dropdowns in pop up can be buttons
the dots on the calander indicate if there is space or not

when booking a day you can select a voucher

we used MELO as inspiration, you are welcome to look at it as well.. screenshots attached

please ask questions if you have any

```html
<!DOCTYPE html>
<html lang="en">
<head>
<meta charset="utf-8">
<title>Book day</title>
<link href="https://fonts.googleapis.com/css2?family=Mulish:wght@400;600;700&display=swap" rel="stylesheet">
<style>
:root{
  --green:#00b14f;
  --ink:#2f3443;
  --ink-soft:#4a4f5c;
  --muted:#a3a7af;
  --faint:#b5b8be;
  --line:#e6e7e9;
  --tile:#f2f3f4;
  --shade:#ececec;
  --white:#ffffff;
}
*{box-sizing:border-box;margin:0;padding:0}
html,body{width:1200px;height:2598px;overflow:hidden;background:var(--white)}
body{font-family:"Mulish",sans-serif;color:var(--ink)}
.screen{position:absolute;left:0;top:0;width:750px;height:1624px;transform:scale(1.6);transform-origin:0 0;background:linear-gradient(#fff 0,#fff 1130px,#e9e9e9 1624px);overflow:hidden}
.abs{position:absolute}
.topbar{left:0;top:0;width:750px;height:7px;background:var(--green)}
.header{left:0;top:7px;width:750px;height:379px;background:linear-gradient(#fff 0,#fff 290px,#efefef 379px)}
.month{left:0;width:750px;top:72px;text-align:center;font-size:29px;color:var(--ink-soft);letter-spacing:.3px}
.month svg{vertical-align:middle;margin-left:12px}
.weekday{top:174px;width:100px;margin-left:-50px;text-align:center;font-size:22px;color:#6e7380;letter-spacing:.5px}
.day{top:232px;width:64px;height:64px;margin-left:-32px;border-radius:50%;border:2px solid #eeeff0;background:#fff;display:flex;align-items:center;justify-content:center;font-size:22px;color:var(--muted)}
.day.is-selected{background:var(--green);border-color:var(--green);color:#fff}
.dot{top:314px;width:6px;height:6px;margin-left:-3px;border-radius:50%;background:#a9acb2}
.dot.is-active{background:var(--green)}
.panel{left:0;top:386px;width:750px;height:760px;background:#fff}
.notch{left:465px;top:372px;width:0;height:0;border-left:14px solid transparent;border-right:14px solid transparent;border-bottom:14px solid #fff}
.title{left:42px;top:452px;font-size:42px;font-weight:400;color:var(--ink)}
.date{right:35px;top:464px;font-size:26px;color:var(--muted)}
.tile{left:28px;width:70px;height:70px;border-radius:18px;background:var(--tile);display:flex;align-items:center;justify-content:center}
.row-label{left:137px;font-size:26px;color:var(--ink)}
.row-value{left:137px;font-size:26px;color:var(--muted)}
.chev{left:698px}
.divider{left:38px;width:673px;height:2px;background:var(--line)}
.bso{left:553px;top:608px;font-size:26px;color:var(--ink)}
.toggle{left:636px;top:604px;width:74px;height:40px;border-radius:20px;background:var(--green)}
.toggle::after{content:"";position:absolute;right:4px;top:4px;width:32px;height:32px;border-radius:50%;background:#fff}
.seg{top:1004px;font-size:26px;color:var(--faint)}
.seg.is-selected{left:137px;top:998px;width:109px;height:50px;border:2px solid var(--green);border-radius:6px;color:var(--ink);display:flex;align-items:center;justify-content:center}
.card{left:30px;top:1189px;width:690px;height:409px;background:#fff;border-radius:8px;box-shadow:0 4px 30px rgba(0,0,0,.07)}
.col{top:1222px;width:200px;margin-left:-100px;text-align:center}
.col-top{height:36px;font-size:24px;color:var(--muted);display:flex;align-items:center;justify-content:center}
.col-label{font-size:22px;color:var(--ink);margin-top:6px}
.vsep{top:1240px;width:1px;height:50px;background:var(--line)}
.hsep{left:60px;top:1339px;width:631px;height:2px;background:var(--line)}
.total{left:0;width:750px;top:1370px;text-align:center;font-size:25px;font-weight:700;color:var(--ink)}
.total-label{left:0;width:750px;top:1416px;text-align:center;font-size:22px;color:var(--ink)}
.btn{top:1487px;width:300px;height:88px;border-radius:4px;display:flex;align-items:center;justify-content:center;font-size:26px;font-weight:600;letter-spacing:.3px}
.btn-cancel{left:64px;background:#eeefef;color:#555a63}
.btn-confirm{left:384px;background:var(--green);color:#fff}
</style>
</head>
<body>
<main class="screen">
  <div class="abs topbar"></div>
  <section class="abs header" aria-label="Calendar">
  </section>

  <svg class="abs" style="left:28px;top:76px" width="34" height="34" viewBox="0 0 34 34"><circle cx="15" cy="15" r="12" fill="none" stroke="#b5b8be" stroke-width="2.2"/><line x1="24" y1="24" x2="32" y2="32" stroke="#b5b8be" stroke-width="2.2" stroke-linecap="round"/></svg>
  <div class="abs month">October 2019<svg width="22" height="12" viewBox="0 0 22 12"><path d="M1 1l10 10L21 1" fill="none" stroke="#b5b8be" stroke-width="2"/></svg></div>
  <svg class="abs" style="left:683px;top:75px" width="36" height="36" viewBox="0 0 36 36"><rect x="0" y="3" width="15" height="15" rx="2" fill="#b9bcc2"/><rect x="0" y="21" width="15" height="15" rx="2" fill="#b9bcc2"/><rect x="18" y="21" width="15" height="15" rx="2" fill="#b9bcc2"/><rect x="19" y="1" width="13" height="13" rx="2" fill="#b9bcc2" transform="rotate(45 25.5 7.5)"/></svg>

  <div class="abs weekday" style="left:62px">MON</div>
  <div class="abs weekday" style="left:165px">TUE</div>
  <div class="abs weekday" style="left:269px">WED</div>
  <div class="abs weekday" style="left:371px">THU</div>
  <div class="abs weekday" style="left:478px">FRI</div>
  <div class="abs weekday" style="left:581px">SAT</div>
  <div class="abs weekday" style="left:685px">SUN</div>

  <div class="abs day" style="left:63px">14</div>
  <div class="abs day" style="left:161px">15</div>
  <div class="abs day" style="left:272px">16</div>
  <div class="abs day" style="left:375px">17</div>
  <div class="abs day is-selected" style="left:479px">18</div>
  <div class="abs day" style="left:580px">19</div>
  <div class="abs day" style="left:684px">20</div>

  <div class="abs dot" style="left:63px"></div>
  <div class="abs dot" style="left:269px"></div>
  <div class="abs dot is-active" style="left:478px"></div>

  <section class="abs panel" aria-label="Booking"></section>
  <div class="abs notch"></div>

  <h1 class="abs title">Book day</h1>
  <div class="abs date">01 Sep 2019</div>

  <div class="abs tile" style="top:590px"><svg width="28" height="26" viewBox="0 0 28 26"><rect x="0" y="0" width="12" height="11" rx="1.5" fill="#b9bcc2"/><rect x="0" y="14" width="12" height="11" rx="1.5" fill="#b9bcc2"/><rect x="15" y="14" width="12" height="11" rx="1.5" fill="var(--green)"/></svg></div>
  <div class="abs row-label" style="top:592px">Availability</div>
  <div class="abs row-value" style="top:630px">1m/1a left</div>
  <div class="abs bso">BSO</div>
  <div class="abs toggle" role="switch" aria-checked="true"></div>
  <div class="abs divider" style="top:696px"></div>

  <div class="abs tile" style="top:728px"><svg width="22" height="28" viewBox="0 0 22 28"><path d="M11 1C5.5 1 1.5 5 1.5 10.3 1.5 17 11 27 11 27s9.5-10 9.5-16.7C20.5 5 16.5 1 11 1z" fill="var(--green)"/><circle cx="11" cy="10.5" r="3.6" fill="#fff"/></svg></div>
  <div class="abs row-label" style="top:721px">Location</div>
  <div class="abs row-value" style="top:761px">RBW</div>
  <svg class="abs chev" style="top:753px" width="14" height="22" viewBox="0 0 14 22"><path d="M2 2l9 9-9 9" fill="none" stroke="#8d9199" stroke-width="2"/></svg>
  <div class="abs divider" style="top:827px"></div>

  <div class="abs tile" style="top:856px"><svg width="28" height="28" viewBox="0 0 28 28"><circle cx="14" cy="8" r="6" fill="var(--green)"/><path d="M1 27c0-7 6-11 13-11s13 4 13 11z" fill="var(--green)"/></svg></div>
  <div class="abs row-label" style="top:851px">Group</div>
  <div class="abs row-value" style="top:891px">3-Penguins</div>
  <svg class="abs chev" style="top:880px" width="14" height="22" viewBox="0 0 14 22"><path d="M2 2l9 9-9 9" fill="none" stroke="#8d9199" stroke-width="2"/></svg>
  <div class="abs divider" style="top:957px"></div>

  <div class="abs tile" style="top:988px"><svg width="28" height="28" viewBox="0 0 28 28"><circle cx="14" cy="14" r="13" fill="var(--green)"/><path d="M13 6v9h7" fill="none" stroke="#fff" stroke-width="2.6" stroke-linecap="round"/></svg></div>
  <div class="abs seg is-selected">Full</div>
  <div class="abs seg" style="left:294px">AM</div>
  <div class="abs seg" style="left:397px">PM</div>
  <div class="abs seg" style="left:519px">Flex</div>
  <div class="abs seg" style="left:616px">Try</div>

  <section class="abs card" aria-label="Summary"></section>
  <div class="abs col" style="left:139px"><div class="col-top">$100.00</div><div class="col-label">Price</div></div>
  <div class="abs vsep" style="left:246px"></div>
  <div class="abs col" style="left:374px"><div class="col-top"><svg width="84" height="32" viewBox="0 0 84 32"><path d="M1 4h38v7a5 5 0 0 0 0 10v7H1v-7a5 5 0 0 0 0-10z" fill="none" stroke="#9a9ea6" stroke-width="2"/><line x1="11" y1="12" x2="27" y2="12" stroke="#9a9ea6" stroke-width="2"/><line x1="11" y1="20" x2="27" y2="20" stroke="#9a9ea6" stroke-width="2"/><circle cx="66" cy="16" r="16" fill="var(--green)"/><path d="M59 16l5 5 9-10" fill="none" stroke="#fff" stroke-width="2.6" stroke-linecap="round" stroke-linejoin="round"/></svg></div><div class="col-label">Voucher</div></div>
  <div class="abs vsep" style="left:486px"></div>
  <div class="abs col" style="left:587px"><div class="col-top"><svg width="40" height="10" viewBox="0 0 40 10"><circle cx="5" cy="5" r="4" fill="none" stroke="#9a9ea6" stroke-width="1.6"/><circle cx="20" cy="5" r="4" fill="none" stroke="#9a9ea6" stroke-width="1.6"/><circle cx="35" cy="5" r="4" fill="none" stroke="#9a9ea6" stroke-width="1.6"/></svg></div><div class="col-label">Options</div></div>
  <div class="abs hsep"></div>
  <div class="abs total">$100.00</div>
  <div class="abs total-label">Total</div>
  <div class="abs btn btn-cancel">Cancel Booking</div>
  <div class="abs btn btn-confirm">Confirm Booking</div>
</main>
</body>
</html>
```